distributor of aftermarket auto electrical components

I am after business card design for my new company called
Summit Vehicle Supplies (SVS as the acronym). I will supplying automotive wiring components, basically from battery to headlight. I will be aiming to sell in the 4wd scene and to auto electricians. i am not worried which colours are used though i would like it to be dynamic.
Updates

sorry guys, i have add a mobile and e-mail address that will need to on there as well. Sorry for theĀ inconvenience.

sorry guys i had erred on my spelling with my e-mail. i have now fixed it in the brief

Target Market(s)

4wd industry, custom cars, RV, auto electricians

Industry/Entity Type

Electrical

Requirements
Must have
• Company Name
ABN number: 71 306 548 290
Director: Derek Holloway
M 0432 718 946
E dhollo@fernwire.com.au

```html
<!DOCTYPE html>
<html lang="en">
<head>
<meta charset="utf-8">
<title>Summit Vehicle Supplies – Business Card</title>
<link rel="stylesheet" href="https://fonts.googleapis.com/css2?family=Ubuntu:wght@700&family=Noto+Serif:ital,wght@1,400;1,700&family=Cabin:wght@600&display=swap">
<style>
  :root {
    --ink: #1b1b1b;
    --black: #000000;
    --white: #ffffff;
    --red: #ff0000;
    --steel: #c8c8c8;
  }
  * { margin: 0; padding: 0; box-sizing: border-box; }
  html, body { width: 888px; height: 1200px; overflow: hidden; background: var(--white); }
  .canvas { position: relative; width: 888px; height: 1200px; }

  .card { position: absolute; left: 2px; width: 884px; overflow: hidden; }

  .wordmark {
    position: absolute; left: 0; right: 0;
    font-family: "Ubuntu", sans-serif; font-weight: 700;
    font-size: 290px; line-height: 1; text-align: center; letter-spacing: 10px;
    transform: scaleX(1.35); transform-origin: center;
  }
  .company-name {
    position: absolute; left: 0; right: 0;
    font-family: "Ubuntu", sans-serif; font-weight: 700;
    font-size: 52px; line-height: 1; text-align: center; letter-spacing: 4px;
    color: var(--red);
  }

  /* Front */
  .card--front { top: 2px; height: 520px; border: 1.5px solid var(--black); background: var(--white); }
  .card--front .wordmark { top: 8px; color: var(--ink); }
  .card--front .company-name { top: 268px; }
  .divider { position: absolute; left: 0; right: 0; top: 324px; height: 5px; background: var(--black); }
  .director {
    position: absolute; left: 0; right: 0; top: 342px; text-align: center;
    font-family: "Noto Serif", serif; font-style: italic; color: var(--black);
  }
  .director__label { font-size: 28px; font-weight: 400; }
  .director__name { font-size: 46px; font-weight: 700; }
  .contact {
    position: absolute; left: 20px; top: 420px;
    font-family: "Cabin", sans-serif; font-weight: 600;
    font-size: 26px; line-height: 40px; color: var(--black);
  }
  .contact__key { color: var(--red); margin-right: 6px; }
  .abn {
    position: absolute; right: 18px; top: 454px;
    font-family: "Cabin", sans-serif; font-weight: 600;
    font-size: 36px; line-height: 1.2; color: var(--red);
  }

  /* Back */
  .card--back { top: 679px; height: 518px; background: var(--white); }
  .band { position: absolute; left: 0; right: 0; }
  .band--black { background: var(--black); }
  .band--steel { background: var(--steel); }
  .card--back .wordmark { top: 86px; color: var(--white); }
  .card--back .company-name { top: 362px; }
</style>
</head>
<body>
<div class="canvas">

  <section class="card card--front">
    <div class="wordmark">SVS</div>
    <div class="company-name">Summit Vehicle Supplies</div>
    <div class="divider"></div>
    <p class="director"><span class="director__label">director: </span><span class="director__name">Derek Holloway</span></p>
    <div class="contact">
      <p class="contact__line"><span class="contact__key">M</span>0432 718 946</p>
      <p class="contact__line"><span class="contact__key">E</span>dhollo@fernwire.com.au</p>
    </div>
    <p class="abn">ABN: 71 306 548 290</p>
  </section>

  <section class="card card--back">
    <div class="band band--black" style="top:0;height:48px"></div>
    <div class="band band--black" style="top:55px;height:5px"></div>
    <div class="band band--steel" style="top:62px;height:6px"></div>
    <div class="band band--black" style="top:72px;height:383px"></div>
    <div class="band band--steel" style="top:458px;height:6px"></div>
    <div class="band band--black" style="top:468px;height:5px"></div>
    <div class="band band--black" style="top:478px;height:40px"></div>
    <div class="wordmark">SVS</div>
    <div class="company-name">Summit Vehicle Supplies</div>
  </section>

</div>
</body>
</html>
```